Business Card Design, including supply of raw art files plus a vector diagram of the zelvon logo and

We need the business card design for a company that is launching a new exciting product. The brief requires the submission of the following once the final design is chosen:

- business card layout including raw files
- a composite vector image file of the zelvon logo and tag line
- a standalone vector image file of the zelvon logo

The product will be launched as a customer engagement app.

It has 4 core modules which enables a person to do multiple things - book tours and activities, order takeaways, search for local deals and offers. A universal currency is at the heart of this product. When you use the app, you earn cashback rewards when shopping or buying at any of the merchant partners across the modules as . These rewards can then be used as full or part payment when buying goods or services at these merchant partners.

The business card must help us build the brand, communicate the benefit of the brand's key focus - the ability to earn and burn this universal cashback ccurrency - across the 4 modules - booking of tours and activities, ordering, searching for local deals and payment.

We would like the design to use the brand's blue colour the hex colour is: 00
Dark grey : 646464
Darker blue shadow: 058bdd
Main Blue: 0084ff

We need to translate this into a CMYK print or spot colour print.

Both print options to be supplied as separate files.

An example of the base concept we have in mind is attached for your reference.

The font used by the brand is Proxima Nova.

Note: the duration has been set as 2 days.

Industry/Entity Type

Business

Contact Information for Business Card

Carla Mendoza
Marketing
W: www.zelvon.example
M: + 61 400555123
T: +61 2 5550 1473
A: Suite 7, Level 2, 14-18 Harwick Street, Sydney, NSW, 2000, Australia

Font styles to use
Sans Serif

Requirements
Must have
• zelVon logo and tagline
• address details
• zelVon icons as supplied
Nice to have
• would like to have the option of a spot varnish layer over the logo and icons at the back of the card

```html
<!DOCTYPE html>
<html lang="en">
<head>
<meta charset="utf-8">
<title>zelVon business card</title>
<link href="https://fonts.googleapis.com/css2?family=Open+Sans:wght@300;400;600;700&display=swap" rel="stylesheet">
<style>
  :root {
    --brand-blue: #2f8fd6;
    --brand-blue-deep: #1f78c0;
    --card-white: #ffffff;
    --card-dark: #353535;
    --ink: #3a3a3a;
    --ink-soft: #8a8a8a;
    --stage: #e6e6e6;
  }
  * { margin: 0; padding: 0; box-sizing: border-box; }
  html, body { width: 1200px; height: 716px; overflow: hidden; }
  body {
    background: var(--stage);
    font-family: "Open Sans", Arial, sans-serif;
    position: relative;
  }
  .card {
    position: absolute;
    top: 200px;
    width: 540px;
    height: 316px;
    overflow: hidden;
    box-shadow: 0 6px 18px rgba(0,0,0,.18);
  }

  /* Front */
  .card-front { left: 40px; background: var(--card-white); color: var(--ink); }
  .brand { position: absolute; display: flex; align-items: center; }
  .brand-dot { border-radius: 50%; background: var(--brand-blue); flex: none; }
  .card-front .brand { left: 30px; top: 24px; }
  .card-front .brand-dot { width: 44px; height: 44px; margin-right: 10px; }
  .card-front .brand-name { font-size: 38px; font-weight: 300; color: var(--ink); line-height: 1; }
  .tagline {
    position: absolute; left: 86px; top: 68px;
    font-size: 12px; font-weight: 300; color: var(--ink-soft);
  }
  .address {
    position: absolute; left: 40px; top: 112px;
    font-size: 12.5px; line-height: 18px; font-style: normal;
  }
  .phones { position: absolute; left: 40px; top: 172px; list-style: none; font-size: 12.5px; line-height: 20px; }
  .phones li { display: flex; align-items: center; gap: 7px; }
  .phones svg { width: 13px; height: 13px; }
  .person { position: absolute; right: 34px; top: 200px; text-align: right; }
  .person-name { font-size: 17px; font-weight: 700; color: var(--brand-blue); }
  .person-role { font-size: 14px; color: var(--ink); }
  .front-band { position: absolute; left: 0; bottom: 0; width: 540px; height: 64px; }
  .front-url {
    position: absolute; right: 44px; bottom: 12px;
    color: var(--card-white); font-size: 16px; letter-spacing: 3px;
  }

  /* Back */
  .card-back { left: 620px; background: var(--card-dark); color: var(--card-white); }
  .card-back .brand { left: 150px; top: 118px; }
  .card-back .brand-dot { width: 56px; height: 56px; margin-right: 12px; }
  .card-back .brand-name { font-size: 54px; font-weight: 300; color: var(--card-white); line-height: 1; }
  .back-url {
    position: absolute; left: 120px; top: 248px;
    font-size: 16px; letter-spacing: 4px;
  }
  .modules { position: absolute; right: 20px; top: 18px; list-style: none; }
  .module { display: flex; flex-direction: column; align-items: flex-end; margin-bottom: 10px; }
  .module-icon {
    width: 44px; height: 44px; border-radius: 50%; background: var(--brand-blue);
    display: flex; align-items: center; justify-content: center; margin-right: 18px;
  }
  .module-icon svg { width: 24px; height: 24px; }
  .module-label { font-size: 10.5px; margin-top: 4px; }
</style>
</head>
<body>

<section class="card card-front" aria-label="Business card front">
  <div class="brand">
    <span class="brand-dot"></span>
    <span class="brand-name">zelVon</span>
  </div>
  <p class="tagline">rewards everywhere</p>

  <address class="address">
    Suite 7, Level 2,<br>
    14-18 Harwick Street, Sydney,<br>
    NSW, 2000, Australia
  </address>

  <ul class="phones">
    <li>
      <svg viewBox="0 0 14 14"><circle cx="7" cy="7" r="7" fill="var(--brand-blue)"/><rect x="4.5" y="3" width="5" height="8" rx="1" fill="none" stroke="#fff" stroke-width="1.1"/></svg>
      + 61 400555123
    </li>
    <li>
      <svg viewBox="0 0 14 14"><circle cx="7" cy="7" r="7" fill="var(--brand-blue)"/><path d="M4 5.5h6v4H4z M5 4h4v1.5H5z" fill="#fff"/></svg>
      +61 2 5550 1473
    </li>
  </ul>

  <div class="person">
    <p class="person-name">Carla Mendoza</p>
    <p class="person-role">Marketing</p>
  </div>

  <svg class="front-band" viewBox="0 0 540 64" preserveAspectRatio="none" aria-hidden="true">
    <polygon points="0,22 90,22 110,4 470,4 500,22 540,22 540,64 0,64" fill="var(--brand-blue-deep)"/>
    <polygon points="0,26 540,26 540,64 0,64" fill="var(--brand-blue)"/>
  </svg>
  <p class="front-url">www.zelvon.example</p>
</section>

<section class="card card-back" aria-label="Business card back">
  <div class="brand">
    <span class="brand-dot"></span>
    <span class="brand-name">zelVon</span>
  </div>
  <p class="back-url">www.zelvon.example</p>

  <ul class="modules">
    <li class="module">
      <span class="module-icon">
        <svg viewBox="0 0 24 24" fill="none" stroke="#fff" stroke-width="1.8" stroke-linecap="round">
          <path d="M7 3v7M5 3v4a2 2 0 0 0 4 0V3M7 10v11"/>
          <ellipse cx="16" cy="7" rx="2.5" ry="4"/><path d="M16 11v10"/>
        </svg>
      </span>
      <span class="module-label">Mobile Ordering</span>
    </li>
    <li class="module">
      <span class="module-icon">
        <svg viewBox="0 0 24 24" fill="none" stroke="#fff" stroke-width="1.8" stroke-linecap="round">
          <path d="M14.5 5.5c-.5-1-1.5-1.5-2.5-1.5-1.5 0-2.5.8-2.5 2s1 1.7 2.5 2 2.5.8 2.5 2-1 2-2.5 2c-1 0-2-.5-2.5-1.5M12 2.5v1.5M12 12v1.5"/>
          <path d="M3 17h4l3 2h5l5-3"/>
        </svg>
      </span>
      <span class="module-label">CashBack Rewards</span>
    </li>
    <li class="module">
      <span class="module-icon">
        <svg viewBox="0 0 24 24"><path d="M4 8h3l2-2.5h6L17 8h3v11H4z" fill="#fff"/><circle cx="12" cy="13" r="3.3" fill="var(--brand-blue)"/></svg>
      </span>
      <span class="module-label">Tours &amp; Activities</span>
    </li>
    <li class="module">
      <span class="module-icon">
        <svg viewBox="0 0 24 24"><path d="M4 12l8-8h7v7l-8 8z" fill="#fff"/><circle cx="16" cy="7.5" r="1.4" fill="var(--brand-blue)"/></svg>
      </span>
      <span class="module-label">Local Offers</span>
    </li>
  </ul>
</section>

</body>
</html>
```